Lebel for 500g Honey Jar

We want a design for a 500g honey bottle or Jar as shown in the attached image . All Requirement has been put in the attached brief document .
Also Logo and images have been uploaded . Feel free to play arround with the selected solor schemes .

Target Market(s)

Retail Market

Industry/Entity Type

FMCG

Colors
00AB8E
00BBA5
67D7C9
C6EFE9
E9F9F6
59FF00
82FF00
B8FF75
E3FFCB
F4FFEA
FFC000
F8CF3A
FAE287
FDF2CF
FEFAEE
F0912C
F2A743
F7CA91
FBE8D2
FDF5EE
EE7325
F08F49
F5BC92
FAE3D3
FDF4ED

Requirements
Must have
• The desing must contain the company Address, Logo , and Nutritional Facts
Nice to have
• Image of a honey Bee , see samples attahed

```html
<!DOCTYPE html>
<html lang="en">
<head>
<meta charset="utf-8">
<title>Meadowly Pure Honey – 500g Jar Label</title>
<link rel="stylesheet" href="https://fonts.googleapis.com/css2?family=Sniglet:wght@800&family=Source+Sans+3:wght@400;600&family=Poppins:wght@500&display=swap">
<style>
  :root {
    --page-bg: #ffffff;
    --label-yellow: #fdd535;
    --label-yellow-deep: #f8c81e;
    --honey-light: #fbe08a;
    --honey-mid: #f5bc2a;
    --honey-deep: #e9a412;
    --leaf-white: #ffffff;
    --ink: #141414;
    --pill-ink: #0d0d0d;
    --pill-text: #ffffff;
    --comb-tint: #fde35a;
  }
  * { box-sizing: border-box; margin: 0; padding: 0; }
  html, body {
    width: 1200px; height: 1200px; overflow: hidden;
    background: var(--page-bg);
  }
  .label {
    position: absolute; left: 285px; top: 75px;
    width: 630px; height: 1050px;
    background: linear-gradient(180deg, var(--label-yellow) 0%, var(--label-yellow) 55%, var(--comb-tint) 100%);
    box-shadow: 0 6px 18px rgba(0,0,0,0.28);
    overflow: hidden;
    font-family: "Source Sans 3", sans-serif;
    color: var(--ink);
  }
  .honey-drips {
    position: absolute; left: 0; top: 0; width: 630px; height: 400px;
    background: linear-gradient(180deg, var(--honey-mid) 0%, var(--honey-light) 38%, rgba(253,213,53,0) 100%);
  }
  .comb-field {
    position: absolute; left: 0; top: 700px; width: 630px; height: 350px;
    background: linear-gradient(180deg, rgba(253,227,90,0) 0%, rgba(255,236,120,0.7) 100%);
  }
  .brand-leaf { position: absolute; left: 0; top: 0; width: 630px; height: 280px; }
  .brand-name {
    position: absolute; left: 0; width: 630px; top: 92px;
    padding-left: 120px;
    text-align: center;
    font-family: "Poppins", sans-serif; font-weight: 500;
    font-size: 62px; letter-spacing: 1px; color: var(--ink);
  }
  .product-title {
    position: absolute; left: 0; width: 630px; top: 430px;
    text-align: center;
    font-family: "Sniglet", sans-serif; font-weight: 800;
    color: var(--ink); line-height: 1;
  }
  .product-title .pure { display: block; font-size: 88px; }
  .product-title .honey { display: block; font-size: 138px; letter-spacing: 4px; margin-top: -4px; }
  .purity-pill {
    position: absolute; left: 150px; top: 688px; width: 330px; height: 44px;
    border-radius: 22px; background: var(--pill-ink);
    color: var(--pill-text); font-size: 24px;
    display: flex; align-items: center; justify-content: center;
  }
  .claims {
    position: absolute; left: 0; width: 630px; top: 762px;
    text-align: center; font-size: 28px; line-height: 35px;
  }
  .divider {
    position: absolute; left: 167px; top: 855px; width: 296px; height: 2px;
    background: linear-gradient(90deg, rgba(20,20,20,0) 0%, var(--ink) 30%, var(--ink) 70%, rgba(20,20,20,0) 100%);
  }
  .distributor {
    position: absolute; left: 0; width: 630px; top: 889px;
    text-align: center; font-size: 21px; line-height: 28px; font-weight: 600;
  }
  .net-weight {
    position: absolute; left: 0; width: 630px; top: 988px;
    text-align: center; font-size: 15px;
  }
  .net-weight strong { font-size: 27px; font-weight: 600; }
</style>
</head>
<body>
  <main class="label">
    <div class="honey-drips" role="img" aria-label="Golden honey dripping down from a honeycomb along the top edge"></div>
    <div class="comb-field" role="img" aria-label="Faint honeycomb texture across the lower label"></div>

    <svg class="brand-leaf" viewBox="0 0 630 280" aria-hidden="true">
      <path d="M75 262 C110 150 200 50 262 0 L630 0 L630 165 C520 225 300 250 75 262 Z" fill="var(--leaf-white)"/>
    </svg>
    <div class="brand-name">meadowly</div>

    <h1 class="product-title">
      <span class="pure">Pure</span>
      <span class="honey">HONEY</span>
    </h1>

    <div class="purity-pill">100% Pure &amp; Natural</div>

    <p class="claims">Zero additive • Zero colouring<br>• Zero preservative</p>

    <div class="divider"></div>

    <p class="distributor">Packed &amp; Distributed by<br>Brightfield Farms Limited</p>

    <p class="net-weight">Net WT: <strong>500g</strong></p>
  </main>
</body>
</html>
```